continuing medical education travel company. luxury, professional, quality service

PLEASE USE THE REVISED LOGO FOR ALL CARD DESIGNS, NO SNAKE HEAD

Target Market(s)

physicians

Industry/Entity Type

Travel Industry

Contact Information for Business Card

luxury quality, spot uv, foil, rounded corners

Colors
0255a3
3176b5
cfdeed
aaaaaa
5c5c5c

Requirements
Must have
• navy, platinum, possible holographic

```html
<!DOCTYPE html>
<html lang="en">
<head>
<meta charset="utf-8">
<title>Aurelis Travel – Business Cards</title>
<link rel="stylesheet" href="https://fonts.googleapis.com/css2?family=Roboto:wght@400;500;700&display=swap">
<style>
  :root {
    --navy: #2d2a8c;
    --navy-deep: #23217a;
    --platinum: #aaaaaa;
    --graphite: #5c5c5c;
    --paper: #ffffff;
    --backdrop: #e9e9ee;
  }
  * { box-sizing: border-box; margin: 0; padding: 0; }
  html, body {
    width: 1200px; height: 950px; overflow: hidden;
    background: var(--backdrop);
    font-family: "Roboto", Arial, sans-serif;
  }
  .stage { position: relative; width: 1200px; height: 950px; }
  .card {
    position: absolute; width: 700px; height: 400px;
    border-radius: 26px; overflow: hidden;
    box-shadow: 0 10px 28px rgba(0,0,0,.22);
  }
  .brand { display: flex; flex-direction: column; font-weight: 500; text-transform: uppercase; line-height: 1; }
  .brand-main { letter-spacing: 6px; }
  .brand-sub { letter-spacing: 14px; }

  .card--back {
    left: 90px; top: 45px;
    background: linear-gradient(135deg, var(--navy) 0%, var(--navy-deep) 100%);
    display: flex; flex-direction: column; align-items: center; justify-content: center;
    color: var(--paper);
  }
  .card--back .brand { align-items: center; color: var(--paper); }
  .card--back .brand-main { font-size: 54px; }
  .card--back .brand-sub { font-size: 22px; margin-top: 12px; margin-right: -14px; }
  .card--back .website {
    margin-top: 36px; font-size: 17px; letter-spacing: 4px; color: var(--paper);
  }

  .card--front { left: 410px; top: 505px; background: var(--paper); }
  .card--front .wave { position: absolute; inset: 0; }
  .card--front .brand { position: absolute; left: 46px; top: 112px; color: var(--navy); }
  .card--front .brand-main { font-size: 40px; }
  .card--front .brand-sub { font-size: 16px; margin-top: 10px; letter-spacing: 12px; }
  .person { position: absolute; left: 46px; top: 232px; }
  .person-name { font-size: 25px; font-weight: 700; color: var(--navy); }
  .person-role { font-size: 18px; color: var(--platinum); margin-top: 4px; }
  .contact {
    position: absolute; right: 34px; top: 120px;
    text-align: right; color: var(--paper); font-size: 16px; line-height: 1.35;
  }
  .address { margin-bottom: 18px; }
  .contact-row { display: flex; justify-content: flex-end; align-items: center; gap: 10px; }
  .contact-row svg { width: 16px; height: 16px; flex: none; }
</style>
</head>
<body>
<main class="stage">
  <section class="card card--back" aria-label="Card back">
    <div class="brand"><span class="brand-main">Aurelis</span><span class="brand-sub">Travel</span></div>
    <div class="website">www.aurelistravel.com</div>
  </section>

  <section class="card card--front" aria-label="Card front">
    <svg class="wave" viewBox="0 0 700 400" preserveAspectRatio="none" aria-hidden="true">
      <path fill="var(--platinum)" d="M415,0 C300,70 360,250 225,320 C150,360 60,362 0,362 L0,400 L700,400 L700,0 Z"/>
      <path fill="var(--paper)" d="M428,0 C318,72 376,258 240,330 C165,370 70,376 0,376 L0,400 L700,400 L700,0 Z"/>
      <path fill="none" stroke="var(--navy)" stroke-width="3" d="M436,0 C328,74 386,262 250,336 C175,376 80,382 0,382"/>
      <path fill="var(--navy)" d="M450,0 C345,78 400,270 265,344 C190,384 90,390 0,390 L0,400 L700,400 L700,0 Z"/>
    </svg>

    <div class="brand"><span class="brand-main">Aurelis</span><span class="brand-sub">Travel</span></div>
    <div class="person">
      <div class="person-name">Laura Bennett</div>
      <div class="person-role">Principal</div>
    </div>

    <div class="contact">
      <div class="address">12 Harbour Lane<br>Lakeview<br>QC H0H 2A4</div>
      <div class="contact-row"><span>555.010.4827</span>
        <svg viewBox="0 0 16 16"><path fill="#fff" d="M3 1h3l1 4-2 1c1 2 3 4 5 5l1-2 4 1v3c0 1-1 2-2 2C7 15 1 9 1 3c0-1 1-2 2-2z"/></svg>
      </div>
      <div class="contact-row"><span>lbennett@aurelistravel.com</span>
        <svg viewBox="0 0 16 16"><rect x="1" y="3" width="14" height="10" fill="#fff"/><path d="M1 3l7 6 7-6" fill="none" stroke="var(--navy)" stroke-width="1.4"/></svg>
      </div>
      <div class="contact-row"><span>www.aurelistravel.com</span>
        <svg viewBox="0 0 16 16"><circle cx="8" cy="8" r="7" fill="#fff"/><path d="M1 8h14M8 1c-3 4-3 10 0 14M8 1c3 4 3 10 0 14" fill="none" stroke="var(--navy)" stroke-width="1.2"/></svg>
      </div>
    </div>
  </section>
</main>
</body>
</html>
```